2-Sided Checklist

I need well designed checklist. This will be handed out by insurance agents, wealth managers, and estate planners as a way to instruct their clients on organization and planning. The checklist features and To Do list on one side and an advertisement for services on the other. The checklist should be easy to read, showcase a professional design, and feature our logo on the back.

I've included the checklist copy and logo in the uploaded files.

Target Market(s)

Insurance Agents and Wealth Managers will hand these out to their clients (typically 40-65 y/o)

Requirements
Must have
• Must include the logo and text
• Must be in MS Word for updates and printability

```html
<!DOCTYPE html>
<html lang="en">
<head>
<meta charset="utf-8">
<title>Keepwell – Life Document Checklist</title>
<link rel="stylesheet" href="https://fonts.googleapis.com/css2?family=Lato:wght@400;700&family=Merriweather:wght@400&display=swap">
<style>
  :root {
    --brand-blue: #4ba5cd;
    --ink: #2e2e2e;
    --brand-name: #4b9fcc;
    --paper: #ffffff;
    --backdrop: #e9e4dc;
    --box-line: #3a3a3a;
  }
  * { box-sizing: border-box; margin: 0; padding: 0; }
  html, body {
    width: 1200px; height: 1200px; overflow: hidden;
    background: var(--backdrop);
  }
  .checklist-card {
    position: absolute;
    left: 320px; top: 40px;
    width: 630px; height: 1260px;
    background: var(--paper);
    transform: scale(0.8889);
    transform-origin: 0 0;
    box-shadow: 0 6px 18px rgba(0,0,0,0.18);
    font-family: "Merriweather", Georgia, serif;
    color: var(--ink);
  }
  .card-header { position: absolute; left: 0; top: 0; width: 630px; height: 205px; }
  .title-panel {
    position: absolute; inset: 0;
    background: var(--brand-blue);
    clip-path: polygon(405px 0, 630px 0, 630px 205px, 300px 205px);
  }
  .card-title {
    position: absolute; right: 68px; top: 38px;
    font-family: "Lato", Arial, sans-serif; font-weight: 700;
    font-size: 36px; line-height: 45px; text-align: right;
    color: var(--paper);
  }
  .brand {
    position: absolute; left: 68px; top: 78px;
    display: flex; align-items: center; gap: 14px;
  }
  .brand-dot { width: 54px; height: 54px; border-radius: 50%; background: var(--brand-blue); }
  .brand-name {
    font-family: "Lato", Arial, sans-serif; font-weight: 700;
    font-size: 40px; color: var(--brand-name);
  }
  .intro {
    position: absolute; left: 67px; top: 270px; width: 500px;
    font-size: 19.5px; line-height: 26px;
  }
  .section { position: absolute; left: 67px; width: 500px; }
  .section-title {
    font-family: "Lato", Arial, sans-serif; font-weight: 400;
    font-size: 25px; color: var(--brand-blue); height: 38px; line-height: 30px;
  }
  .items {
    display: grid; grid-template-columns: 264px 236px;
    grid-auto-rows: 48.5px; grid-auto-flow: column;
    list-style: none;
  }
  .items.rows-4 { grid-template-rows: repeat(4, 48.5px); }
  .items.rows-5 { grid-template-rows: repeat(5, 48.5px); }
  .item { display: flex; align-items: flex-start; gap: 10px; font-size: 17px; line-height: 20px; }
  .box {
    flex: none; width: 32px; height: 32px;
    border: 2px solid var(--box-line);
    box-shadow: -1px 1px 1px rgba(0,0,0,0.25);
  }
  .label { padding-top: 4px; }
  .label.two-line { padding-top: 0; line-height: 20px; }
  .blank { flex: 1; height: 20px; border-bottom: 1.5px solid var(--ink); margin-right: 0; }
  .insurance { top: 375px; }
  .health { top: 629px; }
  .legacy { top: 883px; }
  .footer-band { position: absolute; left: 0; bottom: 0; width: 630px; height: 69px; background: var(--brand-blue); }
</style>
</head>
<body>
<main class="checklist-card">
  <header class="card-header">
    <div class="title-panel"></div>
    <div class="brand"><span class="brand-dot"></span><span class="brand-name">Keepwell</span></div>
    <h1 class="card-title">Life<br>Document<br>Checklist</h1>
  </header>

  <p class="intro">Everyone should have the following information securely stored and available to family members and trusted advisors.</p>

  <section class="section insurance">
    <h2 class="section-title">Insurance</h2>
    <ul class="items rows-4">
      <li class="item"><span class="box"></span><span class="label">Life</span></li>
      <li class="item"><span class="box"></span><span class="label">Health</span></li>
      <li class="item"><span class="box"></span><span class="label">Home Owners</span></li>
      <li class="item"><span class="box"></span><span class="label">Automotive</span></li>
      <li class="item"><span class="box"></span><span class="label">Umbrella</span></li>
      <li class="item"><span class="box"></span><span class="label">Final Expenses</span></li>
      <li class="item"><span class="box"></span><span class="blank"></span></li>
      <li class="item"><span class="box"></span><span class="blank"></span></li>
    </ul>
  </section>

  <section class="section health">
    <h2 class="section-title">Health/Accident</h2>
    <ul class="items rows-4">
      <li class="item"><span class="box"></span><span class="label">Medical History</span></li>
      <li class="item"><span class="box"></span><span class="label">Medications</span></li>
      <li class="item"><span class="box"></span><span class="label">Allergies</span></li>
      <li class="item"><span class="box"></span><span class="label">Advanced Directives</span></li>
      <li class="item"><span class="box"></span><span class="label two-line">Medical Contacts<br>(GP, specialists)</span></li>
      <li class="item"><span class="box"></span><span class="label two-line">Emergency Contacts<br>(family, friends)</span></li>
      <li class="item"><span class="box"></span><span class="blank"></span></li>
      <li class="item"><span class="box"></span><span class="blank"></span></li>
    </ul>
  </section>

  <section class="section legacy">
    <h2 class="section-title">Legacy</h2>
    <ul class="items rows-5">
      <li class="item"><span class="box"></span><span class="label">Final Will</span></li>
      <li class="item"><span class="box"></span><span class="label">Trust</span></li>
      <li class="item"><span class="box"></span><span class="label">Burial Instructions</span></li>
      <li class="item"><span class="box"></span><span class="label">Digital Footprint</span></li>
      <li class="item"><span class="box"></span><span class="label">Financial Accounts</span></li>
      <li class="item"><span class="box"></span><span class="label">Property Investments</span></li>
      <li class="item"><span class="box"></span><span class="label">Business Ownership</span></li>
      <li class="item"><span class="box"></span><span class="blank"></span></li>
      <li class="item"><span class="box"></span><span class="blank"></span></li>
    </ul>
  </section>

  <footer class="footer-band"></footer>
</main>
</body>
</html>
```